Detail Shop Business card design

i need a business card design for my new detailing company called 'Brenner's Detail Shop'. i want an all black and white design . simple, direct and to the point. i want the designer to choose a fitting font to match the logothe front should have logo, address, phone and email and the back side should have a slogan and text indicating that we offer services on anything including cars, trucks, motorcycles and RVs. slogan will read "we take pride in your ride"
maybe also very small on the back side the IG icon with Brenners_Detail_Shop

phone 482.615.7734
address 7384 E Harlow Ave
Spokane WA 99342
email: BrennersDetail@quorvail.com

Target Market(s)

all ages , auto enthusiasts

Industry/Entity Type

Automotive

Contact Information for Business Card

the front should have logo, address, phone and email and the back side should have a slogan and text indicating that we offer services on anything including cars, trucks, motorcycles and RVs. slogan will read "we take pride in your ride"

phone 482.615.7734
address 7384 E Harlow Ave
Spokane WA 99342

Colors
000000
ffffff

Requirements
Must have
• bold font and very simple design with good spacing
Nice to have
• anything creative from the designer indicating we service any types of vehicles
Should not have
• any colors ,

```html
<!DOCTYPE html>
<html lang="en">
<head>
<meta charset="utf-8">
<title>Brenner's Detail Shop — Business Card</title>
<link href="https://fonts.googleapis.com/css2?family=Lato:wght@400;700;900&display=swap" rel="stylesheet">
<style>
  :root {
    --ink: #000000;
    --paper: #f7f7f7;
    --white: #ffffff;
    --stage: #3a3a3a;
    --rule: #8a8a8a;
  }
  * { margin: 0; padding: 0; box-sizing: border-box; }
  html, body { width: 1200px; height: 802px; overflow: hidden; }
  body {
    background: var(--stage);
    font-family: "Lato", Arial, sans-serif;
    position: relative;
  }
  .card {
    position: absolute;
    top: 274px;
    width: 443px;
    height: 264px;
    overflow: hidden;
  }
  .card--front { left: 136px; background: var(--paper); color: var(--ink); }
  .card--back  { left: 624px; background: var(--ink); color: var(--white); }

  .front__band {
    position: absolute; left: 0; right: 0; bottom: 0;
    height: 12px; background: var(--ink);
  }
  .brand {
    position: absolute; left: 44px; top: 60px;
    display: flex; align-items: center; gap: 10px;
  }
  .brand__dot {
    width: 40px; height: 40px; border-radius: 50%;
    background: var(--ink); flex: none;
  }
  .brand__name {
    font-weight: 900; font-size: 19px; line-height: 1.1;
    color: var(--ink);
  }
  .contact {
    position: absolute; left: 230px; top: 138px;
    font-size: 13.5px; line-height: 17px;
  }
  .contact__row { display: flex; align-items: center; gap: 4px; white-space: nowrap; }
  .contact__row svg { flex: none; }
  .contact__address { margin-top: 6px; }
  .contact__social { margin-top: 8px; font-size: 12.5px; gap: 7px; }
  .social-dot { width: 17px; height: 17px; border-radius: 50%; background: var(--ink); flex: none; }

  .back__services {
    position: absolute; left: 0; right: 0; top: 56px;
    text-align: center; font-size: 18px; line-height: 31px;
  }
  .back__rule {
    position: absolute; left: 86px; width: 270px; top: 192px;
    height: 1px; background: var(--rule);
  }
  .back__slogan {
    position: absolute; left: 0; right: 0; top: 210px;
    text-align: center; font-size: 17.5px; letter-spacing: 0.2px;
  }
</style>
</head>
<body>
  <section class="card card--front">
    <div class="brand">
      <span class="brand__dot"></span>
      <span class="brand__name">Brenner's<br>Detail Shop</span>
    </div>
    <div class="contact">
      <div class="contact__row">
        <svg width="11" height="10" viewBox="0 0 11 10" aria-hidden="true"><path d="M1 3 Q5.5 -1 10 3 L8.5 4.5 L7 3.2 L4 3.2 L2.5 4.5 Z M2.5 5 L8.5 5 L9.5 9.5 L1.5 9.5 Z" fill="#000"/></svg>
        <span>482.615.7734</span>
      </div>
      <div class="contact__row">
        <svg width="11" height="9" viewBox="0 0 11 9" aria-hidden="true"><rect x="0.5" y="1" width="10" height="7" fill="#000"/><path d="M0.5 1 L5.5 5 L10.5 1" stroke="#f7f7f7" stroke-width="1" fill="none"/></svg>
        <span>BrennersDetail@quorvail.com</span>
      </div>
      <div class="contact__address">
        7384 E Harlow Ave<br>Spokane WA 99342
      </div>
      <div class="contact__row contact__social">
        <span class="social-dot"></span>
        <span>Brenners_Detail_Shop</span>
      </div>
    </div>
    <div class="front__band"></div>
  </section>

  <section class="card card--back">
    <p class="back__services">
      We offer services on<br>
      anything including<br>
      cars, trucks, motorcycles<br>
      and RVs.
    </p>
    <div class="back__rule"></div>
    <p class="back__slogan">WE TAKE PRIDE IN YOUR RIDE</p>
  </section>
</body>
</html>
```